****Business Card Design for Cormorant Ridge. Design based around attached logo/company name

I’m looking for business card design for my company Cormorant Ridge Holdings,LLC. Design should be professional, sharp and minimal. Outside of the attached logos, greyscale colors for remainder of cards. My thoughts are two-sided card with attached logo on one side and my info on the other but open to one-sided as well with right design.
Target Market(s)
Real estate professionals including banks, private investors, property owners, developers, commercial tenants like Brewloft, Grocana or Tandberry’s.
Industry/Entity Type
Commercial real estate development and investments.
Contact Information for Business Card
Name, title, email, phone #’s, web address and physical address
Font styles to use
Other font styles liked:
- Helvetica, Garamond, etc
Colors
Designer to choose only greyscale colors for use in the design.
Requirements
Must have
- Attached logo first or second options.
Nice to have
- Two sided card with logo on one side. Attached Logo/company name can be laid out any way that flows as long as it’s legible.name
Should not have
- No loud colors. ***Please do not include logo, I have removed the company design with a logo image.

```html
<!DOCTYPE html>
<html lang="en">
<head>
<meta charset="utf-8">
<title>Cormorant Ridge Holdings – Business Card</title>
<link href="https://fonts.googleapis.com/css2?family=Roboto:wght@400&display=swap" rel="stylesheet">
<style>
  :root {
    --page: #ffffff;
    --card: #5c6475;
    --ink: #ffffff;
    --mark: #9aa0ac;
    --icon: #9aa0ac;
    --rule: #aab0bb;
    --shadow: rgba(0, 0, 0, 0.28);
  }
  html, body {
    margin: 0;
    width: 1200px;
    height: 2317px;
    overflow: hidden;
    background: var(--page);
    font-family: "Roboto", Arial, sans-serif;
  }
  .sheet {
    position: relative;
    width: 1200px;
    height: 2317px;
  }
  .card {
    position: absolute;
    left: 183px;
    width: 834px;
    height: 476px;
    background: var(--card);
    box-shadow: 0 24px 40px var(--shadow);
    color: var(--ink);
  }
  .card--front { top: 650px; }
  .card--back { top: 1190px; }

  .wordmark {
    position: absolute;
    margin: 0;
    color: var(--mark);
    font-weight: 400;
    text-transform: uppercase;
    letter-spacing: 0.08em;
    line-height: 1.15;
  }
  .card--front .wordmark {
    left: 94px;
    top: 92px;
    font-size: 20px;
  }
  .card--back .wordmark {
    left: 0;
    right: 0;
    top: 205px;
    text-align: center;
    font-size: 26px;
  }
  .wordmark span { display: block; }

  .tagline {
    position: absolute;
    left: 94px;
    top: 217px;
    width: 289px;
    margin: 0;
    padding-bottom: 6px;
    border-bottom: 1px solid var(--rule);
    font-size: 16px;
    line-height: 20px;
  }
  .owner {
    position: absolute;
    left: 94px;
    top: 291px;
    margin: 0;
    font-size: 16px;
  }
  .contacts {
    position: absolute;
    left: 94px;
    top: 338px;
    margin: 0;
    padding: 0;
    list-style: none;
    font-size: 13px;
  }
  .contacts li {
    display: flex;
    align-items: center;
    height: 20px;
  }
  .contacts svg {
    width: 14px;
    height: 14px;
    margin-right: 20px;
    fill: none;
    stroke: var(--icon);
    stroke-width: 1.2;
  }
</style>
</head>
<body>
<main class="sheet">
  <section class="card card--front" aria-label="Card front">
    <p class="wordmark"><span>Cormorant Ridge</span><span>Holdings, LLC</span></p>
    <p class="tagline">Commercial real estate development and investments.</p>
    <p class="owner">WONER NAME</p>
    <ul class="contacts">
      <li>
        <svg viewBox="0 0 14 14" aria-hidden="true"><path d="M3 1.5 L5 4 L4 5.5 Q5.5 8.5 8.5 10 L10 9 L12.5 11 L11 12.5 Q5 12 1.5 3 Z"/></svg>
        1234567890
      </li>
      <li>
        <svg viewBox="0 0 14 14" aria-hidden="true"><rect x="1.5" y="3" width="11" height="8"/><path d="M1.5 3 L7 8 L12.5 3"/></svg>
        www.your websitethere.com
      </li>
      <li>
        <svg viewBox="0 0 14 14" aria-hidden="true"><circle cx="7" cy="7" r="5.5"/><ellipse cx="7" cy="7" rx="2.4" ry="5.5"/><path d="M1.5 7 H12.5"/></svg>
        infoyourmailthere@mailhub.com
      </li>
    </ul>
  </section>

  <section class="card card--back" aria-label="Card back">
    <p class="wordmark"><span>Cormorant Ridge</span><span>Holdings, LLC</span></p>
  </section>
</main>
</body>
</html>
```